Civil Engineering Business Card Design

We need a business card design for an Civil Engineering Company located in Naples, Florida. The company name is Morrow Engineering.
What we do:
Site Evaluation
Review existing site conditions and zoning
Evaluation of potential development options
Evaluation of environmental permitting challenges
Prepare alternative master site development or redevelopment plan
Calculate cost and time lines for site development
Address political, environmental, social, and economic impacts of site development
Site Design
Prepare master site development plans
Zoning, rezoning, and zoning amendments for land use changes
Evaluate zoning and environmental permitting challenges
Value engineer alternative land development design and products
Residential Development
Plat development and design
Homeowner association document development
Single family development ranging from affordable housing to large estate projects
Multi family development ranging from duplexes to large scale condominiums
Amenity facilities such as golf courses, parks and clubhouse sites
Commercial Development
Office site and park designs development plans
Industrial site and park development plans
Shopping center site development design
Hospital site design development
Institutional Development
School design development and redevelopment plans
Park design development and enhancement plans
Downtown redevelopment plans for new and existing structures
Theater and park plan development
Parking garage design development
Governmental administration building design
Design Services
Site development
Environmental assessment
Roadway alignment and development
Surface water management
Drainage design
Water distribution system
Fire service analysis
Sewage collection systems
Sewage pump station and force main design
Cable utility conduit layout
Construction details
Construction documents
Technical specifications
Alternative methods and materials analysis
Services During Construction
Development of bid documents
Solicitation and processing of bids
Cost review and analysis
Construction cost estimating
Onsite construction observation
Coordination of field modifications to address unforeseen site conditions
Assess value engineering design and contract work
Review of pay requests and shop drawings
Review of warranties
Development assessment of onsite and offsite mitigation
Verification of construction completion, close out, and certification
Processing final pay requests and turn over
We want a clean design on a white background. We have a current logo but are not happy with it so changes would be greatly appreciated.
Industry/Entity Type
Construction
Contact Information for Business Card
Morrow Engineering
Practical Site Solutions Grounded in Trust and Expertise
Leonard Morrow, President
4870 Bellwood Parkway East
Suite 417C
Harlow Springs, GA 34102
555-364-1905-Office, 555-490-6172-Mobile
Leo@MorrowEng.example, www.MorrowEng.example

```html
<!DOCTYPE html>
<html lang="en">
<head>
<meta charset="utf-8">
<title>Morrow Engineering — Business Card</title>
<link href="https://fonts.googleapis.com/css2?family=Open+Sans:wght@400;600;700&display=swap" rel="stylesheet">
<style>
  :root {
    --page-bg: #e9e9e9;
    --card-bg: #ffffff;
    --ink: #111111;
    --ink-soft: #333333;
    --ink-muted: #6f6f6f;
    --rule: #2a2a2a;
    --band: #0d0d0d;
    --band-text: #ffffff;
    --plan-tone: #f1f1f1;
  }
  * { box-sizing: border-box; margin: 0; padding: 0; }
  html, body {
    width: 1200px; height: 900px; overflow: hidden;
    background: var(--page-bg);
    font-family: "Open Sans", sans-serif;
  }
  .stage {
    width: 1200px; height: 900px;
    display: flex; align-items: center; justify-content: center;
  }
  .card {
    position: relative;
    width: 470px; height: 822px;
    background: var(--card-bg);
    overflow: hidden;
    box-shadow: 0 6px 24px rgba(0,0,0,0.18);
  }
  .plan-backdrop {
    position: absolute; left: 0; right: 0; top: 240px; bottom: 100px;
    background: linear-gradient(160deg, #ffffff 0%, var(--plan-tone) 45%, #ffffff 100%);
  }
  .brand {
    position: absolute; top: 72px; left: 0; right: 0;
    display: flex; align-items: center; justify-content: center; gap: 14px;
  }
  .brand-square { width: 34px; height: 34px; background: var(--ink); }
  .brand-name {
    font-weight: 700; font-size: 30px; color: var(--ink);
    letter-spacing: 1px; text-transform: uppercase; line-height: 1.05;
  }
  .tagline {
    position: absolute; top: 150px; left: 0; right: 0;
    text-align: center; color: var(--ink-muted);
    font-size: 19px; line-height: 1.3;
  }
  .rule-top {
    position: absolute; top: 236px; left: 0; right: 0;
    height: 1px; background: var(--rule);
  }
  .person { position: absolute; top: 268px; left: 0; right: 0; text-align: center; }
  .person-name {
    font-size: 30px; font-weight: 600; color: var(--ink);
    font-variant: small-caps; letter-spacing: 1px;
  }
  .person-role {
    margin-top: 8px;
    display: flex; align-items: center; gap: 12px;
    font-size: 14px; color: var(--ink-soft); letter-spacing: 1.5px;
  }
  .person-role::before, .person-role::after {
    content: ""; height: 1px; background: var(--rule); flex: 1;
  }
  .person-role::after { flex: 0 0 80px; }
  .contact { position: absolute; top: 400px; left: 64px; right: 40px; }
  .contact-group { margin-bottom: 28px; }
  .contact-label {
    font-size: 19px; font-weight: 600; color: var(--ink);
    letter-spacing: 0.5px; text-transform: uppercase;
  }
  .contact-value { font-size: 15.5px; color: var(--ink-soft); line-height: 1.35; }
  .web-band {
    position: absolute; left: 0; right: 0; bottom: 0; height: 100px;
    background: var(--band);
    display: flex; align-items: center; justify-content: center; gap: 16px;
  }
  .web-band::before, .web-band::after {
    content: ""; width: 46px; height: 1px; background: var(--band-text);
  }
  .web-address { color: var(--band-text); font-size: 21px; letter-spacing: 1px; }
</style>
</head>
<body>
  <main class="stage">
    <article class="card">
      <div class="plan-backdrop" role="img" aria-label="Faint site plan drawing in light grey behind the contact details"></div>

      <header class="brand">
        <span class="brand-square"></span>
        <span class="brand-name">Morrow<br>Engineering</span>
      </header>

      <p class="tagline">Practical Site Solutions<br>Grounded in Trust and Expertise</p>

      <div class="rule-top"></div>

      <section class="person">
        <h1 class="person-name">Leonard Morrow</h1>
        <p class="person-role">PRESIDENT</p>
      </section>

      <section class="contact">
        <div class="contact-group">
          <h2 class="contact-label">Address</h2>
          <p class="contact-value">4870 Bellwood Parkway East Suite<br>417C Harlow Springs, GA 30917</p>
        </div>
        <div class="contact-group">
          <h2 class="contact-label">Phone</h2>
          <p class="contact-value">555-364-1905-Office<br>555-490-6172-Mobile</p>
        </div>
        <div class="contact-group">
          <h2 class="contact-label">Email</h2>
          <p class="contact-value">Leo@MorrowEng.example</p>
        </div>
      </section>

      <footer class="web-band">
        <span class="web-address">www.MorrowEng.example</span>
      </footer>
    </article>
  </main>
</body>
</html>
```